Bidlane Display ads for Real Estate Photography

I'm looking for someone to take ideas off of my flyers and website (lensvista27.example) to create two sets of display ads. One for branding and another for specific specials (see magazine-ad-special.pdf). I would like these to be animated gifs that cycle between 2 or 3 views. Here are the dimensions for the ads:
300 x 250 – Inline Rectangle
728 x 90 – Leaderboard
160 x 600 – Wide Skyscraper
320×100 - Large Mobile Banner
I can also provide source artwork from the flyers if needed.
Target Market(s)
Realtors that sell high end luxury homes
Industry/Entity Type
Professional Photography
Requirements
Must have
- .psd source files for each size ad with screens/views on different layers to I can export as an animated gif
- display ads in the following sizes:
- 300 x 250 – Inline Rectangle
- 728 x 90 – Leaderboard
- 160 x 600 – Wide Skyscraper
- 320×100 - Large Mobile Banner
Nice to have
- 336 x 280 – Large Rectangle
- 300 x 600 – Half-Page Ad

```html
<!DOCTYPE html>
<html lang="en">
<head>
<meta charset="utf-8">
<title>LensVista Inline Rectangle Display Ad</title>
<link href="https://fonts.googleapis.com/css2?family=Questrial&family=Didact+Gothic&family=Arimo:wght@400;700&display=swap" rel="stylesheet">
<style>
  :root {
    --page: #ffffff;
    --brand-blue: #1565b0;
    --accent-cyan: #1fb3ea;
    --accent-orange: #f6b25a;
    --size-orange: #ffb25e;
    --band-dark: rgba(62, 52, 44, 0.86);
    --text-light: #ffffff;
  }
  * { margin: 0; padding: 0; box-sizing: border-box; }
  html, body {
    width: 1200px;
    height: 1200px;
    overflow: hidden;
    background: var(--page);
  }
  .canvas {
    position: relative;
    width: 1200px;
    height: 1200px;
  }
  .ad {
    position: absolute;
    left: 164px;
    top: 73px;
    width: 872px;
    height: 725px;
    overflow: hidden;
  }
  .ad__photo {
    position: absolute;
    inset: 0;
    background:
      linear-gradient(180deg, rgba(255,255,255,0) 55%, rgba(120,96,70,0.55) 80%),
      linear-gradient(90deg, #e9ecef 0%, #f7f7f5 30%, #efeae3 55%, #b9a58a 70%, #eeeeec 85%, #d9d4cc 100%);
  }
  .ad__header {
    position: absolute;
    left: 0;
    top: 0;
    width: 872px;
    height: 240px;
  }
  .ad__brand {
    position: absolute;
    left: 26px;
    top: 58px;
    display: flex;
    align-items: center;
    gap: 14px;
    font-family: "Questrial", sans-serif;
    font-size: 64px;
    color: var(--text-light);
    letter-spacing: -1px;
  }
  .ad__brand-dot {
    width: 30px;
    height: 30px;
    border-radius: 50%;
    background: var(--text-light);
  }
  .ad__footer {
    position: absolute;
    left: 0;
    top: 575px;
    width: 872px;
    height: 150px;
    background: var(--band-dark);
  }
  .ad__tagline {
    position: absolute;
    left: 24px;
    top: 14px;
    font-family: "Didact Gothic", "Questrial", sans-serif;
    color: var(--text-light);
    font-size: 46px;
    line-height: 58px;
    letter-spacing: 1.5px;
    white-space: nowrap;
  }
  .ad__tagline-accent {
    color: var(--accent-cyan);
    font-size: 60px;
    letter-spacing: 0;
  }
  .ad__contact {
    position: absolute;
    left: 566px;
    top: 32px;
    width: 296px;
    list-style: none;
    font-family: "Arimo", sans-serif;
    font-weight: 700;
    font-size: 24px;
    color: var(--accent-orange);
  }
  .ad__contact-item {
    display: flex;
    align-items: center;
    gap: 20px;
    height: 46px;
    white-space: nowrap;
  }
  .ad__contact-item svg { width: 32px; height: 32px; flex: none; }
  .size-label {
    position: absolute;
    left: 0;
    top: 858px;
    width: 1200px;
    text-align: center;
    font-family: "Arimo", sans-serif;
    font-size: 160px;
    line-height: 1;
    color: var(--size-orange);
    letter-spacing: 6px;
  }
</style>
</head>
<body>
<main class="canvas">
  <section class="ad">
    <div class="ad__photo" role="img" aria-label="Bright luxury kitchen with white cabinets, stone accent wall, pendant lights and rustic wood islands"></div>

    <svg class="ad__header" viewBox="0 0 872 240" aria-hidden="true">
      <path d="M0,0 H872 V52 Q430 70 0 232 Z" fill="var(--brand-blue)"/>
      <path d="M0,232 Q430 70 872 52" fill="none" stroke="#ffffff" stroke-width="5"/>
    </svg>
    <div class="ad__brand">
      <span class="ad__brand-dot"></span>
      <span class="ad__brand-name">LensVista</span>
    </div>

    <div class="ad__footer">
      <p class="ad__tagline">Grow Your Business<br>&amp; Sell More <span class="ad__tagline-accent">HOMES</span></p>
      <ul class="ad__contact">
        <li class="ad__contact-item">
          <svg viewBox="0 0 24 24"><path fill="#ffffff" d="M6.6 2.5l3 3.6-1.8 2.4c1.2 2.6 3.2 4.7 5.8 5.9l2.3-1.9 3.6 3-1.6 3.2c-.4.7-1.2 1-2 .8C9.3 17.7 5.3 13.6 3.6 6.9c-.2-.8.1-1.6.8-2z"/></svg>
          <span>lensvista27.example</span>
        </li>
        <li class="ad__contact-item">
          <svg viewBox="0 0 24 24"><circle cx="12" cy="12" r="10.5" fill="#ffffff"/><path fill="var(--band-dark)" d="M7 6c2 0 3 1.5 2.5 3S7 11 8 13s-1 3-2.5 2.5C4.5 13 5 8 7 6zm8 2c2 1 2.5 3 1.5 4.5s-3 1-3.5 3 1 3 2.5 3c2.5-1.5 3.5-5 2.5-8z"/></svg>
          <span>555.204.0187</span>
        </li>
      </ul>
    </div>
  </section>

  <p class="size-label">300-250</p>
</main>
</body>
</html>
```